Dale Morven Broker owner of Real Estate Company

Dale Morven, GRI CRS ABR
Broker Owner
555-318-4627
dalemorven@dalemorvenrealtors.example
47362 Larchmont Ave. Fenwick Harbor, MI 49270
Licensed in Michigan and Florida
"37 Years of Outstanding Service based on a Result Driven Marketing Plan"

```html
<!DOCTYPE html>
<html lang="en">
<head>
<meta charset="utf-8">
<title>Dale Morven — Broker Owner</title>
<link href="https://fonts.googleapis.com/css2?family=Arimo:wght@400;700&display=swap" rel="stylesheet">
<style>
  :root {
    --backdrop: #d4d5d7;
    --maroon: #4a1315;
    --divider-grey: #b9babd;
    --ink-light: #ffffff;
    --portrait-top: #f0f0f0;
    --portrait-bottom: #2a3142;
  }
  html, body {
    margin: 0;
    width: 1200px;
    height: 863px;
    overflow: hidden;
    background: var(--backdrop);
    font-family: "Arimo", Arial, sans-serif;
  }
  .business-card {
    position: absolute;
    left: 100px;
    top: 146px;
    width: 1000px;
    height: 571px;
    background: var(--maroon);
    box-shadow: 0 10px 30px rgba(0,0,0,0.18);
    overflow: hidden;
  }
  .card-shapes {
    position: absolute;
    inset: 0;
  }
  .contact-block {
    position: absolute;
    left: 580px;
    top: 0;
    width: 400px;
    height: 571px;
    color: var(--ink-light);
    text-align: center;
    display: flex;
    flex-direction: column;
    justify-content: center;
  }
  .agent-heading {
    display: flex;
    justify-content: center;
    align-items: flex-start;
    gap: 8px;
    margin-bottom: 34px;
  }
  .agent-name {
    font-weight: 700;
    font-size: 30px;
    line-height: 1;
    margin: 6px 0 0;
  }
  .agent-credentials {
    font-size: 16px;
    line-height: 1.25;
    text-align: left;
  }
  .agent-credentials .role { display: block; padding-left: 22px; }
  .contact-line {
    font-size: 18px;
    line-height: 1.35;
    margin: 0;
  }
  .address { margin-bottom: 22px; }
  .contact-icon {
    width: 14px;
    height: 14px;
    vertical-align: -1px;
    margin-left: 7px;
    fill: var(--ink-light);
  }
  .rule {
    width: 32px;
    height: 2px;
    background: var(--ink-light);
    margin: 14px 8px 34px auto;
  }
  .tagline {
    font-size: 18px;
    line-height: 1.35;
    margin: 0;
  }
</style>
</head>
<body>
  <section class="business-card">
    <svg class="card-shapes" width="1000" height="571" viewBox="0 0 1000 571">
      <defs>
        <linearGradient id="portraitTone" x1="0" y1="0" x2="0" y2="1">
          <stop offset="0.45" stop-color="var(--portrait-top)"/>
          <stop offset="1" stop-color="var(--portrait-bottom)"/>
        </linearGradient>
      </defs>
      <polygon class="divider-band" points="0,0 615,0 440,571 0,571" fill="var(--divider-grey)"/>
      <polygon class="portrait-area" points="0,0 588,0 413,571 0,571" fill="url(#portraitTone)"
               role="img" aria-label="Portrait photo of the broker in a dark suit, glasses and patterned tie"/>
    </svg>

    <div class="contact-block">
      <div class="agent-heading">
        <h1 class="agent-name">Dale Morven,</h1>
        <div class="agent-credentials">GRI CRS ABR<span class="role">Broker Owner</span></div>
      </div>

      <p class="contact-line address">47362 Larchmont Ave.<br>Fenwick Harbor, MI 49270</p>

      <p class="contact-line phone">555-318-4627<svg class="contact-icon" viewBox="0 0 16 16" aria-hidden="true"><path d="M3.5 1 6 1.2 7 4.6 5.4 6c.8 1.8 2.3 3.4 4.2 4.3l1.5-1.6 3.4 1v2.6c0 .9-.8 1.7-1.7 1.6C7 13.4 2.5 8.9 1.9 2.7 1.8 1.8 2.6 1 3.5 1z"/></svg></p>
      <p class="contact-line email">dalemorven@dalemorvenrealtors.example<svg class="contact-icon" viewBox="0 0 16 16" aria-hidden="true"><path d="M1 3h14v10H1z M1.6 3.6 8 9l6.4-5.4" stroke="var(--maroon)" stroke-width="1.2"/></svg></p>
      <p class="contact-line licence">Licensed in Michigan &amp; Florida</p>

      <div class="rule"></div>

      <p class="tagline">37 Years of Outstanding Service based<br>on a Result Driven Marketing Plan</p>
    </div>
  </section>
</body>
</html>
```